BANNER AD FOR RUGBY LEAGUE REUINION

MUST BE 605X303 – jpeg format AND 233X233 – jpeg format

(SOME IDEAS - A FOOTBALL FIELD??? A MAGPIE KICKING A GOAL??)

MAGPIE IN PICTURE DOESNT HAVE TO BE USED, IT WAS JUST PUT THERE AS AN IDEA

Target Market(s)

rugby league supporters

Font styles to use
Serif
Sans Serif

Colors

Designer to choose colors to be used in the design.

Requirements
Must have
• MUST HAVE MAGPIE SOMEWHERE ON DESIGN
MUST SAY "RETURN TO CAMPBELLTOWN"
MUST HAVE 12TH JULY AT 7PM
Nice to have
• FOOTBALL OVAL GRASS

```html
<!DOCTYPE html>
<html lang="en">
<head>
<meta charset="utf-8">
<title>Return to Campbelltown – Reunion Banner</title>
<link rel="stylesheet" href="https://fonts.googleapis.com/css2?family=Russo+One&display=swap">
<style>
  :root {
    --paper: #ffffff;
    --ink: #000000;
    --mascot-dark: #111111;
    --mascot-light: #6a6a6a;
  }
  html, body {
    margin: 0;
    padding: 0;
    width: 1200px;
    height: 601px;
    overflow: hidden;
    background: var(--paper);
  }
  .banner {
    position: relative;
    width: 1200px;
    height: 601px;
    background: var(--paper);
  }
  .banner__art {
    position: absolute;
    inset: 0;
  }
  .headline {
    font-family: "Russo One", "Arial Black", sans-serif;
    fill: var(--ink);
  }
  .headline__rule {
    stroke: var(--ink);
    stroke-width: 3;
  }
  .mascot {
    fill: url(#mascotTone);
  }
</style>
</head>
<body>
<main class="banner">
  <svg class="banner__art" viewBox="0 0 1200 601" width="1200" height="601" aria-labelledby="eventTitle">
    <defs>
      <linearGradient id="mascotTone" x1="0" y1="0" x2="1" y2="1">
        <stop offset="0" stop-color="var(--mascot-light)"/>
        <stop offset="0.5" stop-color="var(--mascot-dark)"/>
        <stop offset="1" stop-color="var(--mascot-light)"/>
      </linearGradient>
    </defs>

    <g class="headline" id="eventTitle">
      <text class="headline__lead" x="395" y="256" font-size="78" text-anchor="middle"
            textLength="440" lengthAdjust="spacingAndGlyphs">RETURN TO</text>
      <text class="headline__place" x="395" y="360" font-size="88" text-anchor="middle"
            textLength="728" lengthAdjust="spacingAndGlyphs">CAMPBELLTOWN</text>
      <line class="headline__rule" x1="28" y1="373" x2="762" y2="373"/>
      <text class="headline__date" x="395" y="456" font-size="72" text-anchor="middle"
            textLength="700" lengthAdjust="spacingAndGlyphs" xml:space="preserve">JULY  12TH  7PM</text>
    </g>

    <rect class="mascot" x="838" y="14" width="330" height="478" rx="60"
          role="img" aria-label="Black and white illustration of a magpie mascot in a football jersey, flexing one wing"/>
  </svg>
</main>
</body>
</html>
```